Web and Logo Design - Investing Website

Financial website, so needs to be clean and professional. I like vector images that are simple and professional (data, investing) but do not overpower the website. Will need to show off the charts to emphasize portfolio’s performance. Should be mainly blue and white (does not have to be the blue tones selected). Homepage should have a section where it shows off the three portfolios with a quick summary (see content file) and performance graph (see performance charts file) - with a "learn more" link.

Homepage Header links - Strategies; Monthly Updates; FAQ; Signup; Login

Pages needed:
Homepage
Articles/Blog Main Page
Article Layout Template
Dashboard Template (see Dashboard information file)

Sample designs i like: https://www.plimvaro.io/ - https://www.brastekin.com/ - https://www.holvendarquist.com/

Industry/Entity Type

Finance - Investing

Number of Pages Required

4 page

Colors
0054AA
0677BA
7BADD7
CADEEF
E8F1F8

Requirements
Should not have
• Generic pictures of people

```html
<!DOCTYPE html>
<html lang="en">
<head>
<meta charset="utf-8">
<title>Quantvale Portfolio – Blog Articles</title>
<link href="https://fonts.googleapis.com/css2?family=Barlow:wght@300;400;500;600;700&family=Montserrat:wght@400;500;600&display=swap" rel="stylesheet">
<style>
:root{
  --blue-deep:#0054AA;
  --blue:#0677BA;
  --blue-mid:#7BADD7;
  --blue-soft:#CADEEF;
  --blue-pale:#E8F1F8;
  --ink:#4a5563;
  --footer:#154a97;
  --white:#ffffff;
}
*{box-sizing:border-box;margin:0;padding:0}
html,body{width:1200px;height:2904px;overflow:hidden}
body{position:relative;background:var(--white);font-family:"Montserrat",sans-serif;color:var(--ink)}
a{text-decoration:none;color:inherit}

.site-header{position:absolute;top:0;left:0;width:1200px;height:81px;border-bottom:1px solid #e3e9f0;background:var(--white);z-index:2}
.brand{position:absolute;left:113px;top:22px;display:flex;align-items:center;gap:10px}
.brand-dot{width:36px;height:36px;border-radius:50%;background:var(--blue)}
.brand-name{font-family:"Montserrat",sans-serif;font-weight:600;font-size:19px;line-height:18px;color:var(--blue);letter-spacing:.3px}
.main-nav{position:absolute;top:36px;left:429px;display:flex;gap:47px;font-size:12.5px;font-weight:500;color:var(--blue-deep);letter-spacing:.2px}
.btn-outline,.btn-solid{position:absolute;top:26px;height:35px;width:91px;font-size:11.5px;font-weight:500;display:flex;align-items:center;justify-content:center;letter-spacing:.3px}
.btn-outline{left:868px;border:1.5px solid var(--blue);color:var(--blue-deep)}
.btn-solid{left:964px;background:var(--blue);color:var(--white)}

.hero{position:absolute;top:81px;left:0;width:1200px;height:420px}
.hero-bg{position:absolute;inset:0}
.hero-title{position:absolute;left:118px;top:126px;font-family:"Barlow",sans-serif;font-weight:300;font-size:50px;color:var(--blue-deep)}
.hero-title strong{font-weight:600}
.hero-lead{position:absolute;left:119px;top:194px;width:420px;font-size:16px;line-height:25px;color:#3e4654}
.hero-art{position:absolute;left:600px;top:30px;width:470px;height:390px;border-radius:50% 40% 30% 45%;background:linear-gradient(160deg,#d4e6f5,#a9cdec 60%,#e8f1f8)}

.section-title{position:absolute;top:548px;width:1200px;text-align:center;font-family:"Barlow",sans-serif;font-weight:400;font-size:39px;color:var(--blue-deep)}
.section-title strong{font-weight:600}
.section-rule{position:absolute;top:601px;left:590px;width:56px;height:3px;background:var(--blue)}

.deco-disc{position:absolute;left:85px;top:597px;width:170px;height:165px;border-radius:50%;background:var(--blue-pale)}

.articles{position:absolute;top:654px;left:133px;width:960px}
.article{position:relative;height:294px;margin-bottom:66px}
.article-media{position:absolute;left:0;top:0;width:460px;height:294px;border:1px solid var(--blue-soft);border-radius:3px;background:linear-gradient(160deg,#f6fafd,#dbeaf7 55%,#f3f8fc)}
.article-body{position:absolute;left:497px;top:4px;width:450px}
.article-date{display:inline-block;background:var(--blue-mid);color:var(--white);font-family:"Barlow",sans-serif;font-weight:500;font-size:11.5px;padding:4px 23px;border-radius:12px}
.article-title{margin-top:13px;margin-left:5px;font-family:"Barlow",sans-serif;font-weight:600;font-size:24.5px;line-height:31px;color:var(--blue-deep)}
.article-rule{margin:14px 0 0 5px;width:56px;height:3px;background:var(--blue)}
.article-text{margin:23px 0 0 5px;font-size:13.3px;line-height:19.2px;color:#4f5866}
.read-more{display:inline-flex;margin:23px 0 0 7px;width:133px;height:40px;align-items:center;justify-content:center;background:var(--blue-deep);color:var(--white);font-family:"Barlow",sans-serif;font-weight:500;font-size:14px}

.site-footer{position:absolute;left:0;top:2505px;width:1200px;height:399px}
.site-footer svg{position:absolute;inset:0}
.footer-brand{position:absolute;left:153px;top:136px;display:flex;align-items:center;gap:10px}
.footer-brand .brand-dot{background:var(--white)}
.footer-brand .brand-name{color:var(--white);font-size:21px;line-height:20px}
.footer-col{position:absolute;top:130px;padding-left:30px;border-left:2px solid var(--white);height:20px;font-family:"Barlow",sans-serif;color:var(--white)}
.footer-col h4{font-weight:600;font-size:16.5px;line-height:20px}
.footer-col ul{list-style:none;margin-top:7px}
.footer-col li{font-size:13.5px;line-height:23px;color:#dfe9f6}
.col-nav{left:418px}.col-res{left:641px}.col-touch{left:865px;padding-left:27px}
.socials{display:flex;gap:6px;margin-top:12px}
.socials span{width:25px;height:25px;border-radius:50%;background:var(--white)}
.footer-line{position:absolute;left:0;top:330px;width:1200px;height:1px;background:rgba(255,255,255,.18)}
.copyright{position:absolute;top:354px;width:1200px;text-align:center;font-family:"Barlow",sans-serif;font-size:12px;color:#cbd9ec}
</style>
</head>
<body>

<header class="site-header">
  <a class="brand" href="#"><span class="brand-dot"></span><span class="brand-name">QUANTVALE<br>PORTFOLIO</span></a>
  <nav class="main-nav"><a href="#">STRATEGIES</a><a href="#">MONTHLY UPDATES</a><a href="#">FAQ</a></nav>
  <a class="btn-outline" href="#">SIGN UP</a>
  <a class="btn-solid" href="#">LOGIN</a>
</header>

<section class="hero">
  <svg class="hero-bg" width="1200" height="420" viewBox="0 0 1200 420" aria-hidden="true">
    <defs><linearGradient id="heroGrad" x1="0" y1="0" x2="0" y2="1"><stop offset="0" stop-color="#ffffff"/><stop offset="1" stop-color="#e8f1f8"/></linearGradient></defs>
    <path d="M0 0H1200V355C1100 320 980 300 800 330C600 365 420 425 250 410C120 400 40 370 0 335Z" fill="url(#heroGrad)"/>
  </svg>
  <h1 class="hero-title">Our Blog <strong>Articles</strong></h1>
  <p class="hero-lead">QuantvalePortfolio.com uses market data, factoring and backtesting to make data driven</p>
  <div class="hero-art" role="img" aria-label="Isometric illustration of a laptop showing a blog page, with a person holding a pencil, plant and desk items"></div>
</section>

<h2 class="section-title">Latest <strong>Articles</strong></h2>
<div class="section-rule"></div>
<div class="deco-disc" aria-hidden="true"></div>

<main class="articles">
  <article class="article">
    <div class="article-media" role="img" aria-label="Isometric illustration of a data dashboard platform with connected charts and small figures"></div>
    <div class="article-body">
      <span class="article-date">20 SEP 2021</span>
      <h3 class="article-title">Sed ut perspiciatis unde omnis iste natus error sit voluptatem.</h3>
      <div class="article-rule"></div>
      <p class="article-text">Aorem ipsum dolor sit amet, consectetur adipiscing elit, sed do eius-mod tempor incididunt ut labore et dolore magna liqua. Ut enim ad minim veniam, quis nostrud exercitation ullamco laboris nisi ut aliquip ex ea commodo consequat. Duis aute irure dolor in reprehenderit in voluptate velit esse cillum dolore eu fugiat</p>
      <a class="read-more" href="#">Read More</a>
    </div>
  </article>
  <article class="article">
    <div class="article-media" role="img" aria-label="Illustration of a monitor with bar chart, magnifier, target and analysts"></div>
    <div class="article-body">
      <span class="article-date">10 SEP 2021</span>
      <h3 class="article-title">Avoluptas sit aspernatur aut odit aut fugit consequuntur magni</h3>
      <div class="article-rule"></div>
      <p class="article-text">Aorem ipsum dolor sit amet, consectetur adipiscing elit, sed do eius-mod tempor incididunt ut labore et dolore magna liqua. Ut enim ad minim veniam, quis nostrud exercitation ullamco laboris nisi ut aliquip ex ea commodo consequat. Duis aute irure dolor in reprehenderit in voluptate velit esse cillum dolore eu fugiat</p>
      <a class="read-more" href="#">Read More</a>
    </div>
  </article>
  <article class="article">
    <div class="article-media" role="img" aria-label="Isometric illustration of growth arrow over buildings with small analytics figures"></div>
    <div class="article-body">
      <span class="article-date">05 SEP 2021</span>
      <h3 class="article-title">Nemo enim ipsam voluptatem quia vo-luptas sit aspernatur aut</h3>
      <div class="article-rule"></div>
      <p class="article-text">Aorem ipsum dolor sit amet, consectetur adipiscing elit, sed do eius-mod tempor incididunt ut labore et dolore magna liqua. Ut enim ad minim veniam, quis nostrud exercitation ullamco laboris nisi ut aliquip ex ea commodo consequat. Duis aute irure dolor in reprehenderit in voluptate velit esse cillum dolore eu fugiat</p>
      <a class="read-more" href="#">Read More</a>
    </div>
  </article>
  <article class="article">
    <div class="article-media" role="img" aria-label="Illustration of a large analytics dashboard with gears and two presenters"></div>
    <div class="article-body">
      <span class="article-date">04 SEP 2021</span>
      <h3 class="article-title">Quis autem vel eum iure reprehenderit qui in ea voluptate velit esse</h3>
      <div class="article-rule"></div>
      <p class="article-text">Aorem ipsum dolor sit amet, consectetur adipiscing elit, sed do eius-mod tempor incididunt ut labore et dolore magna liqua. Ut enim ad minim veniam, quis nostrud exercitation ullamco laboris nisi ut aliquip ex ea commodo consequat. Duis aute irure dolor in reprehenderit in voluptate velit esse cillum dolore eu fugiat</p>
      <a class="read-more" href="#">Read More</a>
    </div>
  </article>
  <article class="article">
    <div class="article-media" role="img" aria-label="Isometric illustration of office platforms with a handshake and chart presentation"></div>
    <div class="article-body">
      <span class="article-date">06 SEP 2021</span>
      <h3 class="article-title">Ut enim ad minima veniam, quis nostrum exercitationem ullam</h3>
      <div class="article-rule"></div>
      <p class="article-text">Aorem ipsum dolor sit amet, consectetur adipiscing elit, sed do eius-mod tempor incididunt ut labore et dolore magna liqua. Ut enim ad minim veniam, quis nostrud exercitation ullamco laboris nisi ut aliquip ex ea commodo consequat. Duis aute irure dolor in reprehenderit in voluptate velit esse cillum dolore eu fugiat</p>
      <a class="read-more" href="#">Read More</a>
    </div>
  </article>
</main>

<footer class="site-footer">
  <svg width="1200" height="399" viewBox="0 0 1200 399" aria-hidden="true">
    <defs><linearGradient id="footGrad" x1="0" y1="0" x2="1" y2="1"><stop offset="0" stop-color="#1a4592"/><stop offset="1" stop-color="#0c5aa6"/></linearGradient></defs>
    <path d="M0 70C120 20 260 8 420 12C620 18 820 70 980 60C1080 54 1150 30 1200 8V399H0Z" fill="url(#footGrad)"/>
  </svg>
  <div class="footer-brand"><span class="brand-dot"></span><span class="brand-name">QUANTVALE<br>PORTFOLIO</span></div>
  <div class="footer-col col-nav"><h4>Navigation</h4><ul><li>Strategies</li><li>Monthly updates</li><li>FAQ</li></ul></div>
  <div class="footer-col col-res"><h4>Resources</h4><ul><li>Blog</li><li>Signup</li><li>Login</li><li>Contact</li></ul></div>
  <div class="footer-col col-touch"><h4>Get in touch</h4><div class="socials"><span aria-label="Social link"></span><span aria-label="Social link"></span><span aria-label="Social link"></span><span aria-label="Social link"></span></div></div>
  <div class="footer-line"></div>
  <p class="copyright">© 2021 Company Name | All Rights Reserved</p>
</footer>

</body>
</html>
```